Packaging Design Project

We are looking to have the retail packaging of our RAM and USB 3.0 Drives brought into line with a similar look and feel to our newly designed Digital Media & USB 2.0 Drive packaging.

Please note: A designer has already been chosen for this project, so please don't waste any time on it. We will post new design projects for all in the near future.

Thanks!

Industry/Entity Type

Retail

Requirements
Must have
• The USB 3.0 Drives will need an enhancement that creates a little wow factor difference over the USB 2.0 Drive packaging.
We would like the same or similar type of graph included on the back of the card as we've used on our USB 2.0 Drives, to show what each capacity can store.
Must have room for an indusrty standard barcode.

```html
<!DOCTYPE html>
<html lang="en">
<head>
<meta charset="utf-8">
<title>SuperSpeed USB 3.0 Flash Drive – Retail Card</title>
<link href="https://fonts.googleapis.com/css2?family=Michroma&family=Roboto:wght@500;700&display=swap" rel="stylesheet">
<style>
  :root {
    --backdrop: #e4e4e4;
    --card: #ffffff;
    --red: #cc0a0a;
    --red-deep: #a30000;
    --navy: #0f1f5c;
    --ink: #111111;
  }
  html, body {
    margin: 0;
    padding: 0;
    width: 1200px;
    height: 1200px;
    overflow: hidden;
    background: var(--backdrop);
  }
  .canvas {
    position: relative;
    width: 1200px;
    height: 1200px;
  }
  .pack-card {
    position: absolute;
    left: 320px;
    top: 40px;
    width: 560px;
    height: 1120px;
    background: var(--card);
    border-radius: 24px;
    overflow: hidden;
  }
  .grade {
    position: absolute;
    left: 44px;
    top: 66px;
    margin: 0;
    font-family: "Roboto", sans-serif;
    font-weight: 700;
    font-size: 26px;
    color: var(--ink);
  }
  .capacity {
    position: absolute;
    left: 317px;
    top: 46px;
    width: 201px;
    height: 62px;
    border-radius: 21px;
    background: var(--red);
    color: #fff;
    font-family: "Michroma", sans-serif;
    font-size: 34px;
    line-height: 62px;
    text-align: center;
  }
  .capacity small { font-size: 22px; }
  .headline {
    position: absolute;
    left: 44px;
    top: 126px;
    margin: 0;
    font-family: "Michroma", sans-serif;
    font-weight: 400;
  }
  .headline .tag {
    display: block;
    color: var(--red);
    font-size: 27px;
    line-height: 36px;
  }
  .headline .product {
    display: block;
    color: var(--navy);
    font-size: 58px;
    line-height: 61px;
    letter-spacing: -1px;
  }
  .headline .speed {
    display: block;
    color: var(--red);
    font-size: 23px;
    line-height: 40px;
  }
  .swoosh {
    position: absolute;
    left: 0;
    top: 500px;
    width: 560px;
    height: 400px;
  }
  .os-badge {
    position: absolute;
    left: 46px;
    top: 977px;
    width: 194px;
    height: 47px;
  }
  .brand {
    position: absolute;
    left: 0;
    width: 560px;
    top: 1050px;
    margin: 0;
    text-align: center;
    font-family: "Michroma", sans-serif;
    font-size: 28px;
    color: var(--navy);
    letter-spacing: 1px;
  }
</style>
</head>
<body>
<main class="canvas">
  <section class="pack-card">
    <p class="grade">Premium Grade</p>
    <div class="capacity">8<small>GB</small></div>

    <h1 class="headline">
      <span class="tag">SUPERSPEED</span>
      <span class="product">USB 3.0</span>
      <span class="product">FLASH</span>
      <span class="product">DRIVE</span>
      <span class="speed">UP TO 5GBPS</span>
    </h1>

    <svg class="swoosh" viewBox="0 0 560 400" role="img" aria-label="Red motion-blur streak sweeping across the card">
      <defs>
        <linearGradient id="streak" x1="0" y1="0" x2="0" y2="1">
          <stop offset="0" stop-color="#e02020"/>
          <stop offset="0.5" stop-color="#c40000"/>
          <stop offset="1" stop-color="#8e0000"/>
        </linearGradient>
        <linearGradient id="fade" x1="0" y1="0" x2="1" y2="0">
          <stop offset="0" stop-color="#fff" stop-opacity="0"/>
          <stop offset="1" stop-color="#fff" stop-opacity="0.35"/>
        </linearGradient>
      </defs>
      <path d="M0 104 C180 80 380 60 560 34 L560 288 C380 320 180 350 0 366 Z" fill="url(#streak)"/>
      <path d="M0 104 C180 80 380 60 560 34 L560 288 C380 320 180 350 0 366 Z" fill="url(#fade)"/>
    </svg>

    <svg class="os-badge" viewBox="0 0 194 47" aria-label="Windows and Mac compatible">
      <rect x="1.5" y="6" width="191" height="35" rx="12" fill="#fff" stroke="var(--red)" stroke-width="3"/>
      <text x="38" y="31" text-anchor="middle" font-family="Roboto, sans-serif" font-weight="700" font-size="20" fill="var(--red)">WIN</text>
      <text x="155" y="31" text-anchor="middle" font-family="Roboto, sans-serif" font-weight="700" font-size="20" fill="var(--red)">MAC</text>
      <circle cx="97" cy="23.5" r="23" fill="var(--red)"/>
      <text x="97" y="33" text-anchor="middle" font-family="Roboto, sans-serif" font-weight="700" font-size="28" fill="#fff">&amp;</text>
    </svg>

    <p class="brand">NOVARIA</p>
  </section>
</main>
</body>
</html>
```